Bright Cradle, Accelerator for Healthcare Startups, Grand Opening

Bright Cradle is an accelerator for healthcare startup businesses located in North Chicago, Illinois, USA. On July 16th, 4:30 - 6:30 pm, we are having a Grand Opening of our new location, which is at 2460 Walloway, North Chicago, IL. There will be many local dignitaries in attendance, but most importantly we will be unveiling the healthcare startup businesses that will be in our next cohort. We also have four sponsors, logos attached. Here's our website: http://brightcradle-example.ventures/

Target Market(s)

Investors, Healthcare Professionals, Politicians, Dignitaries

Industry/Entity Type

Healthcare

Requirements
Must have
• Logo, Date, Time, Location, Sponsors.
Nice to have
• Extremely elegant, professional design.
Should not have
• This is NOT and opening for retail. This is very professional.

```html
<!DOCTYPE html>
<html lang="en">
<head>
<meta charset="utf-8">
<title>Bright Cradle – Grand Opening</title>
<link rel="stylesheet" href="https://fonts.googleapis.com/css2?family=Josefin+Sans:wght@400;600&family=Great+Vibes&family=Playfair+Display:ital,wght@1,400&family=Abhaya+Libre:wght@400&display=swap">
<style>
  :root {
    --edge: #1c1c1c;
    --card: #2a2a2a;
    --frame: #3a3a3a;
    --ink-light: #f1f1f1;
    --ink-soft: #d9d9d9;
    --accent: #c8494d;
    --accent-deep: #8e3538;
    --flourish: #4a3232;
    --band: #ffffff;
    --band-ink: #1e1e1e;
  }
  * { box-sizing: border-box; margin: 0; padding: 0; }
  html, body { width: 857px; height: 1200px; overflow: hidden; background: var(--edge); }
  .invitation {
    position: relative; width: 857px; height: 1200px;
    background: var(--edge); padding: 14px;
  }
  .invitation__card {
    position: relative; width: 100%; height: 1026px;
    background: var(--card); overflow: hidden;
  }
  .invitation__frame {
    position: absolute; left: 46px; right: 46px; top: 18px; bottom: 24px;
    border: 1px solid var(--frame);
  }
  .flourish {
    position: absolute; left: 0; top: 0; width: 170px; height: 1026px;
    background: linear-gradient(90deg, rgba(74,50,50,0.55), rgba(74,50,50,0));
  }
  .content { position: absolute; inset: 0; text-align: center; color: var(--ink-light); }
  .brand {
    position: absolute; top: 78px; width: 100%;
    font-family: "Josefin Sans", sans-serif; font-weight: 600;
    font-size: 38px; letter-spacing: 1px; text-transform: uppercase; color: var(--ink-soft);
  }
  .small {
    position: absolute; width: 100%;
    font-family: "Josefin Sans", sans-serif; font-size: 16px; line-height: 22px; color: var(--ink-light);
  }
  .intro { top: 152px; }
  .for-the { top: 230px; }
  .title-script {
    position: absolute; font-family: "Great Vibes", cursive; font-weight: 400; line-height: 1;
  }
  .title-script--grand { left: 150px; top: 300px; font-size: 210px; color: var(--accent); }
  .title-script--opening {
    left: 270px; top: 450px; font-size: 190px;
    background: linear-gradient(180deg, var(--accent), var(--accent-deep));
    -webkit-background-clip: text; background-clip: text; color: transparent;
  }
  .location-intro { top: 740px; }
  .detail {
    position: absolute; width: 100%;
    font-family: "Playfair Display", serif; font-style: italic; font-size: 23px; color: var(--ink-light);
  }
  .address { top: 796px; }
  .time { top: 858px; }
  .date {
    position: absolute; top: 912px; width: 100%;
    font-family: "Abhaya Libre", serif; font-size: 36px; letter-spacing: 3px; color: var(--accent);
  }
  .sponsors {
    position: absolute; left: 14px; right: 14px; top: 1032px; height: 154px;
    background: var(--band); border-top: 5px solid var(--accent);
  }
  .sponsors__label {
    position: absolute; left: 120px; top: 16px;
    font-family: "Josefin Sans", sans-serif; font-size: 16px; color: var(--band-ink);
  }
  .sponsors__list {
    position: absolute; left: 110px; right: 40px; top: 60px; height: 60px;
    display: flex; align-items: center; justify-content: space-between; list-style: none;
  }
  .sponsor {
    display: flex; align-items: center; gap: 8px;
    font-family: "Josefin Sans", sans-serif; font-weight: 600; font-size: 20px; color: var(--band-ink);
  }
  .sponsor__dot { width: 18px; height: 18px; border-radius: 50%; background: var(--band-ink); }
  .sponsor__square { width: 18px; height: 18px; background: var(--band-ink); }
</style>
</head>
<body>
<main class="invitation">
  <section class="invitation__card">
    <div class="flourish" role="img" aria-label="Faint dark red swirling flourish ornament along the left edge"></div>
    <div class="invitation__frame"></div>
    <div class="content">
      <p class="brand">Bright Cradle</p>
      <p class="small intro">requests the presence<br>of your company</p>
      <p class="small for-the">for the</p>
      <h1>
        <span class="title-script title-script--grand">Grand</span>
        <span class="title-script title-script--opening">Opening</span>
      </h1>
      <p class="small location-intro">of a new office location at</p>
      <p class="detail address">2460 Walloway, North Chicago, IL</p>
      <p class="detail time">Half past four in the afternoon</p>
      <p class="date">07 . 16 . 2015</p>
    </div>
  </section>
  <footer class="sponsors">
    <p class="sponsors__label">sponsored by:</p>
    <ul class="sponsors__list">
      <li class="sponsor"><span class="sponsor__dot"></span>Hopwell</li>
      <li class="sponsor">Sugar Lantern</li>
      <li class="sponsor">roastandpour-example.com</li>
      <li class="sponsor"><span class="sponsor__square"></span>Kiln &amp; Co</li>
    </ul>
  </footer>
</main>
</body>
</html>
```